Recently launched Investment banking and Corporate Advisory firm focused and experienced on Selling

We are looking for a dynamic Brochure that can highlight our areas of focus, experience and expertise.
We have a small but seasoned team of professionals in the organisation and want to showcase our ability to provide Growth and / or exit solutions for our clients.
We are a boutique firm and want to focus on showcasing the fact that we strive for excellence and quality and not quantity.

Our core business avtivity at this time is Sell Side M&A services (this means that we sell private businesses). We are unique in our approach to "partnering businesses" with other companies...not just selling them. We focus more on the "strategic fit" of the potential partner rather than the simple valuation that a potential partner (buyer) would place on the company.

We have really been focusing on "GROWTH and EXIT" strategies for private business owners. Customers usually talk to us for 1 of two main reasons. Their businesses are usually very stable or rapidly growing , often to a point where the owners are no longer comfortable running them on their own. They often need capital for expansion or a team to help them expand their business into other countries and markets. for this we look for a solution for them and often it is finding them a strategic partner who will want to buy the majority of the business. There are also the clients that are looking for an exit strategy (typically they are older and getting ready to retire) they are typically seeking for a way to exit the business (sell the business).

A tagline I often use is "Customer Vision" - We see our customers business and needs through their eyes.

Our company website is www.brelvanpartners.com and is a work in progress

Target Market(s)

Business Owners (CEO / Presidents)
Mostly Male
Late 40's to late 60's
Very often they will be Engineers
Very Successful and hard working
Many of them looking for GROWTH solutions
Many of them looking for Retirement
We heavily focus on Oil and Gas Service companies, Oil and Gas manufacturing / oilfield services / Technology Companies and Industrial Companies

Industry/Entity Type

Boutique

Font styles to use
Sans Serif

Colors
f37022
33a6d7

Requirements
Must have
• This must be extremely high quality. The people that will receive these brochures are Presidents and CEO's of companies. Every document we give the customer directly reflects the quality of service we will provide for them.
Nice to have
• Pictures tell a great story and can also tell about the areas of experience and expertise that we have

Ideally we'd be interested in a square shaped marketing document (signifies strength and solidness in the business/opportunity) - either 5x5 or 7x7 size in a 4-6 page (double-sided) saddle-stitched booklet.
We'd like to relay an emotion while also describing our business.

```html
<!DOCTYPE html>
<html lang="en">
<head>
<meta charset="utf-8">
<title>Brelvan Partners – Consulting Services</title>
<link href="https://fonts.googleapis.com/css2?family=Quicksand:wght@300&family=Arimo:wght@400&display=swap" rel="stylesheet">
<style>
  :root {
    --paper: #ffffff;
    --brand-blue: #1a7fc6;
    --tint-blue: #4a9ad3;
    --brand-orange: #f37022;
    --text-light: #ffffff;
    --photo-light: #eef0f1;
    --photo-mid: #cfd4d8;
    --photo-dark: #8d949b;
  }
  html, body {
    margin: 0;
    padding: 0;
    width: 1200px;
    height: 600px;
    overflow: hidden;
    background: var(--paper);
  }
  .spread {
    position: relative;
    width: 1200px;
    height: 600px;
    overflow: hidden;
    font-family: "Arimo", Arial, sans-serif;
    color: var(--text-light);
  }
  .margin-strip {
    position: absolute;
    left: 0; top: 0;
    width: 143px; height: 600px;
    background: var(--paper);
  }
  .brand-mark {
    position: absolute;
    left: 22px; top: 512px;
    display: flex;
    align-items: center;
    gap: 6px;
    font-size: 11px;
    color: var(--brand-blue);
    white-space: nowrap;
  }
  .brand-mark .dot {
    width: 12px; height: 12px;
    border-radius: 50%;
    background: var(--brand-orange);
  }
  .content-panel {
    position: absolute;
    left: 143px; top: 0;
    width: 458px; height: 600px;
    background: var(--brand-blue);
  }
  .photo {
    position: absolute;
    left: 601px; top: 0;
    width: 599px; height: 600px;
    background: linear-gradient(90deg, var(--photo-light) 0%, var(--photo-mid) 55%, var(--photo-light) 80%, var(--photo-dark) 100%);
  }
  .photo-tint {
    position: absolute;
    left: 601px; top: 0;
    width: 270px; height: 600px;
    background: linear-gradient(180deg, rgba(34,125,196,0.88), rgba(26,120,194,0.92));
  }
  .title {
    position: absolute;
    left: 170px; top: 52px;
    margin: 0;
    font-family: "Quicksand", Arial, sans-serif;
    font-weight: 300;
    font-size: 52px;
    line-height: 54px;
    letter-spacing: 3px;
  }
  .column {
    position: absolute;
    top: 242px;
    font-size: 11px;
    line-height: 13px;
  }
  .column h2 {
    margin: 0 0 18px;
    font-size: 11px;
    font-weight: 400;
  }
  .column p { margin: 0 0 13px; }
  .column ul {
    list-style: none;
    margin: 0;
    padding: 0 0 0 14px;
  }
  .column li {
    position: relative;
    padding-left: 9px;
  }
  .column li::before {
    content: "";
    position: absolute;
    left: 0; top: 3px;
    width: 6px; height: 6px;
    border-radius: 50%;
    background: var(--text-light);
  }
  .col-growth { left: 172px; width: 192px; }
  .col-exit { left: 379px; width: 200px; }
  .col-exit ul { padding-left: 16px; }
  .col-comms { left: 643px; width: 200px; }
</style>
</head>
<body>
<main class="spread">
  <div class="margin-strip">
    <div class="brand-mark"><span class="dot"></span><span>Brelvan Partners</span></div>
  </div>

  <section class="content-panel" aria-hidden="false"></section>
  <div class="photo" role="img" aria-label="Photograph of two business professionals walking through a bright office corridor"></div>
  <div class="photo-tint"></div>

  <h1 class="title">Consulting<br>Services</h1>

  <section class="column col-growth">
    <h2>Growth Solutions</h2>
    <p>Brelvan Partners can help you put together a strategic plan to grow your business, capitalize on opportunities and maximize performance.</p>
    <p>We will help you achieve measurable business objectives and goals by focusing on outputs and deliverables.</p>
    <p>Our growth solutions include:</p>
    <ul>
      <li>Business performance and process review</li>
      <li>Sales process analysis</li>
      <li>Business analysis</li>
      <li>Activity analysis</li>
      <li>Client and team audits or advisory boards</li>
    </ul>
  </section>

  <section class="column col-exit">
    <h2>Exit Strategies</h2>
    <p>Brelvan Partners can help you devise and implement an exit strategy from your business that puts you in the best possible position as you move toward fulfilling your goals for the future.</p>
    <p>These exit strategies include:</p>
    <ul>
      <li>A plan to improve the value drivers</li>
      <li>A plan to reduce risk</li>
      <li>Process implementation and identification</li>
      <li>Succession planning</li>
      <li>Staff evaluation and management mentoring</li>
      <li>Recasting financials, normalizing profitability</li>
      <li>Creating documentation and business planning</li>
    </ul>
  </section>

  <section class="column col-comms">
    <h2>Communications</h2>
    <p>We focus on developing strong two-way relationships by tailoring appropriate and relevant communications plans to meet the needs that are important to you and your stakeholders.</p>
    <p>We offer a range of communications solutions, including:</p>
    <ul>
      <li>Marketing materials</li>
      <li>Public Relations</li>
      <li>Financial &amp; investor communications</li>
      <li>Crisis communications</li>
      <li>Strategic planning</li>
      <li>Media relations</li>
      <li>Social media strategies</li>
      <li>Executive speeches and presentations</li>
      <li>CSR development</li>
      <li>Ethical decision making seminars</li>
      <li>Special event planning</li>
      <li>Website design</li>
      <li>Writing and editing services</li>
    </ul>
  </section>
</main>
</body>
</html>
```